Solids Control Presentation Template Design

I'm putting together a technical 5-day course about solids control and waste management. I'm looking for an updated art and a easy on the eyes format.

```html
<!DOCTYPE html>
<html lang="en">
<head>
<meta charset="utf-8">
<title>Solids Control Course – Slide Set</title>
<link rel="stylesheet" href="https://fonts.googleapis.com/css2?family=Oswald:wght@500&family=Carlito&family=Open+Sans:wght@600&display=swap">
<style>
  :root{
    --bg-top:#78787c;
    --bg-bottom:#f2f2f3;
    --red:#c00000;
    --brick:#9b2f33;
    --black:#0a0a0a;
    --charcoal:#262626;
    --panel:#545454;
    --grey-mid:#9a9a9a;
    --grey-pie:#7a7a7a;
    --grey-soft:#b3b3b3;
    --grey-light:#d6d6d6;
    --grey-band:#c4c4c4;
    --ink:#222;
    --white:#fff;
  }
  *{margin:0;padding:0;box-sizing:border-box}
  html,body{width:1200px;height:1200px;overflow:hidden}
  body{background:linear-gradient(180deg,var(--bg-top) 0%,#a9a9ac 45%,var(--bg-bottom) 100%);position:relative;font-family:"Carlito",sans-serif}
  .slide{position:absolute;left:310px;width:580px;height:326px;background:var(--white);overflow:hidden;box-shadow:0 2px 6px rgba(0,0,0,.25)}
  .slide--hex{top:40px}
  .slide--pie{top:383px}
  .slide--contact{top:729px;background:var(--panel)}
  .slide svg.shapes{position:absolute;left:0;top:0;width:580px;height:326px}
  .slide-title{position:absolute;left:21px;top:5px;font-family:"Oswald",sans-serif;font-weight:500;font-size:18px;letter-spacing:.2px;color:var(--white);line-height:24px;text-transform:uppercase}
  .slide--contact .slide-title{left:38px}
  .body-copy{position:absolute;left:17px;top:57px;font-size:10.9px;line-height:13px;color:var(--ink);white-space:nowrap}
  .body-copy p+p{margin-top:13px}
  .slide--pie .body-copy{left:18px;top:58px}
  .contact-list{position:absolute;left:14px;top:81px;list-style:none;font-family:"Open Sans",sans-serif;font-weight:600;font-size:12.5px;color:var(--white);line-height:16px}
  .contact-list li{display:flex;align-items:flex-start;gap:9px;margin-bottom:15px}
  .contact-list li svg{flex:none;width:16px;height:16px}
  .page-number{position:absolute;right:3px;bottom:2px;font-family:"Open Sans",sans-serif;font-weight:600;font-size:8px;color:var(--white)}
</style>
</head>
<body>

<!-- Slide: text with hexagon cluster -->
<section class="slide slide--hex">
  <svg class="shapes" viewBox="0 0 580 326" aria-hidden="true">
    <defs>
      <linearGradient id="titleGrad" x1="0" x2="1">
        <stop offset="0" stop-color="#0a0a0a"/><stop offset=".12" stop-color="#0a0a0a"/><stop offset=".55" stop-color="#9b2f33"/><stop offset="1" stop-color="#9b2f33"/>
      </linearGradient>
      <linearGradient id="footGrad" x1="0" x2="1">
        <stop offset="0" stop-color="#9b2f33"/><stop offset=".5" stop-color="#9b2f33"/><stop offset=".62" stop-color="#262626"/><stop offset="1" stop-color="#262626"/>
      </linearGradient>
    </defs>
    <polygon points="0,0 342,0 327,33 0,33" fill="url(#titleGrad)"/>
    <g stroke="#fff" stroke-width="3">
      <polygon points="345,47 385,70 385,116 345,139 305,116 305,70" fill="var(--grey-mid)"/>
      <polygon points="432,47 472,70 472,116 432,139 392,116 392,70" fill="var(--black)"/>
      <polygon points="388,125 428,148 428,194 388,217 348,194 348,148" fill="var(--red)"/>
      <polygon points="476,125 516,148 516,194 476,217 436,194 436,148" fill="var(--grey-light)"/>
      <polygon points="345,204 385,227 385,273 345,296 305,273 305,227" fill="var(--grey-mid)"/>
      <polygon points="432,204 472,227 472,273 432,296 392,273 392,227" fill="var(--grey-soft)"/>
    </g>
    <rect x="0" y="311" width="580" height="15" fill="url(#footGrad)"/>
    <path d="M556,326 A24,24 0 0 1 580,302 L580,326 Z" fill="var(--brick)"/>
  </svg>
  <h2 class="slide-title">Title</h2>
  <div class="body-copy">
    <p>Lorem ipsum dolor sit amet, consectetur adipiscing elit.<br>Sed volutpat pretium pharetra. Maecenas porta diam justo,<br>vitae hendrerit nisi commodo et. Quisque eu metus<br>condimentum, suscipit augue nec, hendrerit enim. Fusce<br>vitae fringilla nisi, ultrices congue urna. In porttitor lacinia<br>mi at accumsan. Donec pharetra mi a sem cursus congue.</p>
    <p>Curabitur suscipit consectetur dolor, sed rhoncus diam<br>porta vel. Sed consequat egestas bibendum. Proin nec<br>ex est. Phasellus rutrum, libero eu consequat semper,<br>felis libero vestibulum odio, sit amet dignissim nulla<br>tortor at urna. Nunc dignissim ullamcorper urna, non<br>vulputate dolor interdum sed. Sed laoreet tempor lectus,<br>dapibus ornare tellus commodo ac. Praesent faucibus<br>tincidunt faucibus. Suspendisse tristique, nisl sit amet<br>sollicitudin laoreet, orci felis scelerisque lectus, ut lobortis<br>tellus est sed eros. In hac habitasse platea dictumst.</p>
  </div>
</section>

<!-- Slide: text with pie chart -->
<section class="slide slide--pie">
  <svg class="shapes" viewBox="0 0 580 326" aria-hidden="true">
    <polygon points="333,0 580,0 580,138 545,311 258,311" fill="var(--grey-band)" stroke="#8fa0b0" stroke-width="1"/>
    <polygon points="0,0 333,0 318,33 0,33" fill="url(#titleGrad)"/>
    <g transform="translate(427,166)">
      <path d="M0,0 L-92.7,53.5 A107,107 0 0 1 0,-107 Z" transform="translate(-3,-2)" fill="var(--grey-pie)"/>
      <path d="M0,0 L92.7,53.5 A107,107 0 0 1 -92.7,53.5 Z" transform="translate(0,4)" fill="var(--black)"/>
      <path d="M0,0 L0,-107 A107,107 0 0 1 92.7,53.5 Z" transform="translate(10,-4)" fill="var(--red)"/>
    </g>
    <rect x="0" y="311" width="580" height="15" fill="url(#footGrad)"/>
    <path d="M556,326 A24,24 0 0 1 580,302 L580,326 Z" fill="var(--brick)"/>
  </svg>
  <h2 class="slide-title">Title</h2>
  <div class="body-copy">
    <p>Lorem ipsum dolor sit amet, consectetur adipiscing elit.<br>Sed volutpat pretium pharetra. Maecenas porta diam justo,<br>vitae hendrerit nisi commodo et. Quisque eu metus<br>condimentum, suscipit augue nec, hendrerit enim. Fusce<br>vitae fringilla nisi, ultrices congue urna. In porttitor lacinia<br>mi at accumsan. Donec pharetra mi a sem cursus congue.</p>
    <p>Curabitur suscipit consectetur dolor, sed rhoncus diam<br>porta vel. Sed consequat egestas bibendum. Proin nec<br>ex est. Phasellus rutrum, libero eu consequat semper,<br>felis libero vestibulum odio, sit amet dignissim nulla<br>tortor at urna. Nunc dignissim ullamcorper urna, non<br>vulputate dolor interdum sed. Sed laoreet tempor lectus,<br>dapibus ornare tellus commodo ac.</p>
  </div>
</section>

<!-- Slide: contact -->
<section class="slide slide--contact">
  <svg class="shapes" viewBox="0 0 580 326" aria-hidden="true">
    <defs>
      <linearGradient id="fieldGrad" x1="0" y1="0" x2="0" y2="1">
        <stop offset="0" stop-color="#6e6e6e"/><stop offset=".35" stop-color="#c9c9c9"/><stop offset=".55" stop-color="#8a8a8a"/><stop offset=".75" stop-color="#222"/><stop offset="1" stop-color="#0b0b0b"/>
      </linearGradient>
    </defs>
    <rect x="0" y="0" width="580" height="38" fill="var(--white)"/>
    <polygon points="0,38 297,38 172,311 0,311" fill="var(--panel)"/>
    <polygon points="346,0 580,0 580,311 172,311 297,38" fill="url(#fieldGrad)" role="img" aria-label="Black and white photo of oilfield pump jacks silhouetted against a bright sky"/>
    <line x1="288" y1="68" x2="170" y2="311" stroke="var(--white)" stroke-width="6"/>
    <polygon points="0,0 346,0 331,34 0,34" fill="url(#titleGrad)"/>
    <rect x="0" y="311" width="580" height="15" fill="url(#footGrad)"/>
    <path d="M556,326 A24,24 0 0 1 580,302 L580,326 Z" fill="var(--brick)"/>
  </svg>
  <h2 class="slide-title">Contact Us</h2>
  <ul class="contact-list">
    <li>
      <svg viewBox="0 0 18 18" aria-hidden="true"><circle cx="9" cy="9" r="8" fill="none" stroke="#c0393d" stroke-width="1.6"/><path d="M9,4.2 a3,3 0 0 1 3,3 c0,2.2 -3,6 -3,6 s-3,-3.8 -3,-6 a3,3 0 0 1 3,-3 z" fill="#fff"/><circle cx="9" cy="7.2" r="1.1" fill="#c0393d"/></svg>
      <span>4850 Millbrook Ave.<br>Riverton, Texas 77500</span>
    </li>
    <li>
      <svg viewBox="0 0 18 18" aria-hidden="true"><circle cx="9" cy="9" r="8" fill="none" stroke="#c0393d" stroke-width="1.6"/><path d="M6,5 l1.6,-.4 1,2.2 -1,.8 a6,6 0 0 0 2.6,2.6 l.8,-1 2.2,1 -.4,1.6 c-3.8,.6 -7.6,-3.2 -6.8,-6.8z" fill="#fff"/></svg>
      <span>555-014-2290</span>
    </li>
    <li>
      <svg viewBox="0 0 18 18" aria-hidden="true"><circle cx="9" cy="9" r="8" fill="none" stroke="#c0393d" stroke-width="1.6"/><rect x="5" y="6" width="8" height="6" fill="#fff"/><path d="M5,6 l4,3.2 4,-3.2" fill="none" stroke="#c0393d" stroke-width=".9"/></svg>
      <span>info@drillcrest-co.com</span>
    </li>
    <li>
      <svg viewBox="0 0 18 18" aria-hidden="true"><circle cx="9" cy="9" r="8" fill="none" stroke="#c0393d" stroke-width="1.6"/><circle cx="9" cy="9" r="4" fill="#fff"/><path d="M5,9 h8 M9,5 c-1.6,2.4 -1.6,5.6 0,8 M9,5 c1.6,2.4 1.6,5.6 0,8" fill="none" stroke="#c0393d" stroke-width=".7"/></svg>
      <span>www.drillcrest-co.com</span>
    </li>
  </ul>
  <span class="page-number">p6</span>
</section>

</body>
</html>
```